Polystyrene Environmental Synopsis

We need a fact sheet for quick reference that groups information units and has a simple but engaging visual presentation of the text and various infographics. We are a trade association representing polystyrene foam manufacturers and this piece is intended to help our members provide effective messaging to their sales personnel.

To view our typical company design/style please see our website at www.foamtradeunion.org. Our primary RGB colors are: (187,140,9); (94,47,29); (94,138,164); and (164,167,15). Secondary RGB colors are (249,162,28) and (218,210,208). Our title/header font is DIN Next LT Pro and our copy font is Calibri 10.5 pt. We can deviate from the font specification if beneficial.

Target Market(s)

Polystyrene manufacturer plant workers and other employees.

Font styles to use
Sans Serif

Requirements
Must have
• Information presentation must be clean and easy to reference.

```html
<!DOCTYPE html>
<html lang="en">
<head>
<meta charset="utf-8">
<title>Polystyrene Environmental Synopsis</title>
<link href="https://fonts.googleapis.com/css2?family=Barlow:wght@600&family=Carlito:ital,wght@0,400;1,400&display=swap" rel="stylesheet">
<style>
  :root {
    --gold: #bb8c09;
    --brown: #5e2f1d;
    --blue: #5e8aa4;
    --olive: #a4a70f;
    --stone: #dad2d0;
    --ink: #2a2a2a;
    --white: #ffffff;
  }
  * { box-sizing: border-box; margin: 0; padding: 0; }
  html, body { width: 928px; height: 1200px; overflow: hidden; background: var(--white); }
  body { position: relative; font-family: "Carlito", "Calibri", sans-serif; color: var(--ink); }

  .org-name {
    position: absolute; left: 54px; top: 58px;
    font-family: "Carlito", "Calibri", sans-serif; font-size: 20px; line-height: 24px;
    color: var(--brown); white-space: nowrap;
  }

  .unit { position: absolute; left: 53px; width: 822px; }
  .unit-tab { position: absolute; left: 0; top: 0; bottom: 0; width: 29px; background: var(--blue); }
  .unit-tab span {
    position: absolute; left: 50%; top: 50%;
    transform: translate(-50%, -50%) rotate(-90deg);
    white-space: nowrap; color: var(--white);
    font-family: "Barlow", sans-serif; font-weight: 600; font-size: 19px;
  }
  .unit-title {
    position: absolute; left: 35px; right: 0; top: 0; height: 34px; background: var(--gold);
    color: var(--white); font-family: "Barlow", sans-serif; font-weight: 600;
    font-size: 18px; display: flex; align-items: center; justify-content: center;
  }
  .col-head {
    position: absolute; top: 42px; height: 29px; background: var(--olive); color: var(--white);
    font-family: "Barlow", sans-serif; font-weight: 600; font-size: 18px;
    display: flex; align-items: center; justify-content: center;
  }
  .col-fact { left: 35px; width: 188px; }
  .col-info { left: 229px; right: 0; }

  .row { position: absolute; left: 35px; right: 0; }
  .fact, .info { position: absolute; top: 0; bottom: 0; background: var(--stone); }
  .fact {
    left: 0; width: 188px; font-style: italic; font-size: 13.5px; line-height: 18.5px;
    text-align: center; padding: 14px 8px 0;
  }
  .info { left: 194px; right: 0; padding: 9px 12px 0 10px; font-size: 13px; line-height: 15.2px; }
  .info ul { list-style: none; }
  .info li { position: relative; padding-left: 9px; }
  .info li::before { content: "•"; position: absolute; left: 0; }
  .info.spaced li { padding-left: 11px; }
  .split { display: flex; gap: 44px; }
  .split ul { width: 154px; }
</style>
</head>
<body>

<header class="org-name">Foam Trade Union</header>

<section class="unit" style="top:208px;height:424px;">
  <div class="unit-tab"><span>Information Unit #1</span></div>
  <h2 class="unit-title">EPS BANS</h2>
  <div class="col-head col-fact">Fact</div>
  <div class="col-head col-info">Supporting Information</div>

  <div class="row" style="top:78px;height:128px;">
    <div class="fact">Material Substitutions<br>Are Risky</div>
    <div class="info"><ul>
      <li>Historically, EPS recycling averages ~18% over a 25-year trendline.</li>
      <li>EPS recycling is most successful in commercial waste streams with large volume sources of EPS waste.</li>
      <li>Consumer access to EPS recycling sometimes requires extra effort, but with proper equipment &amp; handling, it is successful in many communities.</li>
      <li>Creative problem solving for challenging recycling scenarios means Brightmart, NutriWell, Harper Kitchen, Coldstream, Volt Depot, Prairie Cuts are committed to long term EPS recycling.</li>
    </ul></div>
  </div>

  <div class="row" style="top:214px;height:102px;">
    <div class="fact" style="padding-top:30px;">New EPS Recycling<br>Technologies Are Emerging</div>
    <div class="info split">
      <ul><li>Pyrolisis—a chemical reprocessing method—increases the ability to recycle contaminate EPS waste.</li></ul>
      <ul><li>Two new facilities opened in 2018.</li></ul>
    </div>
  </div>

  <div class="row" style="top:322px;height:102px;">
    <div class="fact" style="padding-top:18px;">EPS End-Markets Show<br>Consistent Growth</div>
    <div class="info split">
      <ul><li>It is used as recycled content in new EPS packaging and other EPS products.</li></ul>
      <ul><li>Markets for recycled content EPS include:</li></ul>
    </div>
  </div>
</section>

<section class="unit" style="top:690px;height:424px;">
  <div class="unit-tab"><span>Information Unit #1</span></div>
  <h2 class="unit-title">HUMAN HEALTH &amp; SAFETY</h2>
  <div class="col-head col-fact">Fact</div>
  <div class="col-head col-info">Supporting Information</div>

  <div class="row" style="top:78px;height:128px;">
    <div class="fact">There Is Very Little<br>Residual Styrene in EPS.</div>
    <div class="info"><ul>
      <li>The amount of styrene that might exist in finished polystyrene is extremely small —often lower than naturally occurring styrene found in everyday food items like coffee, strawberries, and cinnamon.</li>
      <li>All chemicals need to be assessed in terms of risk versus exposure. Risks can be zero, negligible or harmful.</li>
    </ul></div>
  </div>

  <div class="row" style="top:213px;height:103px;">
    <div class="fact" style="padding-top:30px;">EPS Is An Organic Polymer</div>
    <div class="info spaced"><ul>
      <li>Polystyrene is an organic compound consisting of hydrogen and carbon.</li>
      <li>Polystyrene is chemically very inert, being resistant to acids and bases but is easily dissolved by many chlorinated solvents, and many aromatic hydrocarbon solvents.</li>
    </ul></div>
  </div>

  <div class="row" style="top:321px;height:103px;">
    <div class="fact" style="padding-top:9px;">EPS Is Safe</div>
    <div class="info spaced"><ul>
      <li>Polystyrene foam is approved for food contact by the FSRA and other global regulatory agencies.</li>
      <li>According to the National Coastal Research Office (NCRO), “although marine debris is a global issue, there are significant gaps in our understanding of the problem.</li>
    </ul></div>
  </div>
</section>

</body>
</html>
```